Business card website / business card for website

We are a French website selling products Made in USA of quality, we need a business card to give from hand to hand and for deposit in the cartons of Each order. We-have the logo That I send in the attachments The theme is: US Vintage and find the compromised entre les national park ambience us and the atmosphere Brooklyn If you can make the feeling it's great The site www.latablederivebleue.com (opening April) You can change the logo a little gold in color it could ... we are a French website selling products Made in USA quality, we need a business card to give from hand to hand and deposit in cartons each order. we have the logo that I convey in the attached parts is the theme: Vintage embiance US and find a compromise between the atmosphere us national park and the atmosphere Brooklyn at: www.latablederivebleue.com (opening April) if you can the impression is great

Target Market(s)

25-50 YEARS man, woman.

Industry/Entity Type

Business

Contact Information for Business Card

www.latablederivebleue.com
N'oubliez pas que nous sommes là si vous avez besoin de nouscontact@latablederivebleue.com

Font styles to use
Serif

Requirements
Must have
• my logo with "general store", my email address preceded by the phrase: Do not forget that we are here if you need us My logo with the words "general store," my email address Preceded by the sentence: remember we're here if you need us (in french)
Nice to have
• i like this style: http://designcorbel.net/ideas/print-ideas/25-charming-old-style-business-card-designs/ must feel the Vintage America it must feel the Vintage America lice can change a little logo or to color ... You can change the logo a little gold in color it could ... i like kraft paper with red ....
Should not have

```html
<!DOCTYPE html>
<html lang="fr">
<head>
<meta charset="utf-8">
<title>La Table de Rive Bleue — Carte de visite</title>
<link rel="stylesheet" href="https://fonts.googleapis.com/css2?family=Roboto+Slab:wght@400;700&family=Source+Sans+3:wght@400&display=swap">
<style>
  :root {
    --backdrop: #ece9e4;
    --kraft-grey: #dddbd6;
    --ink-dark: #2f2f2f;
    --card-black: #151515;
    --ink-light: #f4f4f2;
    --barn-tone: #5b5b5b;
  }
  * { box-sizing: border-box; margin: 0; padding: 0; }
  html, body { width: 1200px; height: 918px; overflow: hidden; }
  body {
    background: var(--backdrop);
    position: relative;
    font-family: "Source Sans 3", sans-serif;
  }
  .card {
    position: absolute;
    left: 250px;
    width: 700px;
    height: 400px;
    border-radius: 4px;
    box-shadow: 0 6px 18px rgba(0,0,0,.18);
    overflow: hidden;
  }
  .card--front { top: 40px; background: var(--kraft-grey); color: var(--ink-dark); }
  .card--back { top: 478px; background: var(--card-black); color: var(--ink-light); }

  /* Front */
  .brand {
    position: absolute;
    left: 0; right: 0; top: 140px;
    display: flex; justify-content: center; align-items: center; gap: 16px;
    font-family: "Roboto Slab", serif;
    font-weight: 700;
    font-size: 26px;
    letter-spacing: 2px;
    text-transform: uppercase;
    white-space: nowrap;
  }
  .brand__dot {
    width: 22px; height: 22px;
    border: 2px solid var(--ink-dark);
    border-radius: 50%;
  }
  .brand__tagline {
    position: absolute;
    left: 0; right: 0; top: 186px;
    text-align: center;
    font-family: "Roboto Slab", serif;
    font-size: 15px;
    letter-spacing: 4px;
    text-transform: uppercase;
  }
  .front__note {
    position: absolute;
    left: 0; right: 0; top: 300px;
    text-align: center;
    font-family: "Roboto Slab", serif;
    font-size: 14px;
    line-height: 24px;
  }

  /* Back */
  .card__rules { position: absolute; inset: 0; }
  .barn-illustration {
    position: absolute;
    left: 270px; top: 40px;
    width: 220px; height: 124px;
    background: linear-gradient(180deg, #2a2a2a 0%, var(--barn-tone) 100%);
    border-radius: 3px 3px 0 0;
  }
  .person__name {
    position: absolute; left: 40px; top: 182px;
    font-family: "Roboto Slab", serif;
    font-size: 21px; letter-spacing: .5px; line-height: 28px;
  }
  .person__role {
    position: absolute; left: 40px; top: 214px;
    font-family: "Roboto Slab", serif;
    font-size: 15px; line-height: 22px;
  }
  .contact {
    position: absolute;
    font-size: 19px; line-height: 30px; letter-spacing: .5px;
    white-space: nowrap;
  }
  .contact--phones { left: 250px; top: 188px; }
  .contact--fax { left: 450px; top: 218px; }
  .contact__web {
    position: absolute; left: 232px; top: 286px;
    font-size: 19px; line-height: 28px; letter-spacing: .3px;
    white-space: nowrap;
  }
</style>
</head>
<body>

<section class="card card--front" aria-label="Recto de la carte">
  <div class="brand"><span class="brand__dot"></span>La Table de Rive Bleue</div>
  <p class="brand__tagline">General Store</p>
  <p class="front__note">N'oubliez pas que nous sommes là si vous avez besoin de nous<br>nouscontact@latablederivebleue.com</p>
</section>

<section class="card card--back" aria-label="Verso de la carte">
  <svg class="card__rules" width="700" height="400" viewBox="0 0 700 400" aria-hidden="true">
    <g stroke="#f4f4f2" stroke-width="2" fill="none">
      <line x1="40" y1="165" x2="660" y2="165"/>
      <line x1="40" y1="300" x2="200" y2="300"/>
      <line x1="510" y1="300" x2="660" y2="300"/>
    </g>
    <g fill="#f4f4f2">
      <polygon points="215,292 217.4,297.5 223,297.8 218.7,301.3 220.2,306.8 215,303.7 209.8,306.8 211.3,301.3 207,297.8 212.6,297.5"/>
      <polygon points="494,292 496.4,297.5 502,297.8 497.7,301.3 499.2,306.8 494,303.7 488.8,306.8 490.3,301.3 486,297.8 491.6,297.5"/>
    </g>
  </svg>

  <div class="barn-illustration" role="img" aria-label="Illustration au trait d'une grange en bois entourée de sapins"></div>

  <p class="person__name">PAUL MARCHAND</p>
  <p class="person__role">CEO/Founder</p>

  <p class="contact contact--phones">P: 612 504 7391<br>C: 745 218 6083</p>
  <p class="contact contact--fax">F: 530 962 4175<br>paul@rivebleuemail.com</p>
  <p class="contact__web">www.latablederivebleue.com</p>
</section>

</body>
</html>
```